Hip, Modern Winery Label+Logo Design Ink Sketch or Print Desired

We need a label and an icon/logo for "TH Wine Co." - a fun, young, hip, modern, small barrel-lot, California Central Coast winery. We will be launching one serious brand (minimal color, serious font), and one fun label. We're open to both.

We'd would like something that looks sketched with an ink pen.

Label/Brand should:
1. Maintain a 3.98(w) x 4.125(h) inch front and back label aspect ratios.
2. The label name (TallhĂ´ve) and logo should be large and legible from across the room. LARGE FONT.

Target Market(s)

26-38yr old, educated, wine drinking adults. Unisex product - although women remain in the lead for purchasing..

Requirements
Must have
• On the front label:
1. Must have a logo or icon of some sort. Using Letters: TH (Wine Co. Optional)
2. Should showcase that we are a young/hip company. Look at the Quillfen logo we've attached..
3. Must contain or have a placeholder for the following: Alcohol/Varietal/Year/Region. (Pick up a bottle of wine if you're curious to see what industry standards are - government requires that Alcohol/Varietal/Year/Region be listed all together on one label - either front or back. We're choosing front.).

Front Label:
a. "Alc. 13.6% by vol."
b. "Clarksburg"
c. "Chenin Blanc"
d. "2012"
e. Create brand logo or icon to Distinguish the Brand from others

Back Label:
One back label will be used for all wines.
Measurements: 3.7466(w) x 4.109 (h)
1. "GOVERNMENT WARNING:" "(1) ACCORDING TO THE SURGEON GENERAL, WOMEN SHOULD NOT DRINK ALCOHOLIC BEVERAGES DURING PREGNANCY BECAUSE OF THE RISK OF BIRTH DEFECTS. (2) CONSUMPTION OF ALCOHOLIC BEVERAGES IMPAIRS YOUR ABILITY TO DRIVE A CAR OR OPERATE MACHINERY, AND MAY CAUSE HEALTH PROBLEMS."
2. "CONTAINS SULFITES"
3. "750 ml"
4. "Vinted & Bottled by TH Wine Co, Buellton, CA".
Nice to have
• Back Label:
Need a map of California lining out the regions we're working with (see design inspiration attachment):

Clarksburg
Lodi
Santa Ynez Valley
Santa Barbara County
Should not have
• No need to provide capsule art. We are planning to place a dollop of wax where the capsule would be - in black or a color that would compliment the label...

No out of date designs please. Something modern, and timeless at the same time (can that be achieved?)

```html
<!DOCTYPE html>
<html lang="en">
<head>
<meta charset="utf-8">
<title>TallhĂ´ve Wine Co. – Chenin Blanc Label</title>
<link rel="stylesheet" href="https://fonts.googleapis.com/css2?family=Tinos&family=Arimo&display=swap">
<style>
  :root {
    --paper: #ffffff;
    --ink: #000000;
    --varietal-red: #e2262b;
    --scene-light: #d9d9d9;
    --scene-dark: #4a4a4a;
  }
  html, body {
    margin: 0;
    padding: 0;
    width: 1200px;
    height: 1177px;
    overflow: hidden;
    background: var(--paper);
  }
  .label {
    position: relative;
    width: 1200px;
    height: 1177px;
    background: var(--paper);
    color: var(--ink);
    font-family: "Tinos", "Times New Roman", serif;
  }
  .frame-outer {
    position: absolute;
    left: 123px;
    top: 79px;
    width: 962px;
    height: 1001px;
    box-sizing: border-box;
    border: 11px solid var(--ink);
  }
  .frame-middle {
    position: absolute;
    left: 140px;
    top: 96px;
    width: 928px;
    height: 967px;
    box-sizing: border-box;
    border: 6px solid var(--ink);
  }
  .frame-inner {
    position: absolute;
    left: 154px;
    top: 110px;
    width: 900px;
    height: 939px;
    box-sizing: border-box;
    border: 2px solid var(--ink);
  }
  .vintage {
    position: absolute;
    left: 0;
    width: 100%;
    top: 128px;
    text-align: center;
    font-size: 48px;
    line-height: 1;
  }
  .vineyard-scene {
    position: absolute;
    left: 354px;
    top: 205px;
    width: 491px;
    height: 450px;
    box-sizing: border-box;
    border: 3px solid var(--ink);
    background: linear-gradient(180deg, var(--paper) 0%, var(--paper) 22%, var(--scene-light) 40%, var(--scene-dark) 100%);
  }
  .brand-name {
    position: absolute;
    left: 0;
    width: 100%;
    top: 770px;
    text-align: center;
    font-size: 56px;
    line-height: 1;
    letter-spacing: 1px;
  }
  .varietal {
    position: absolute;
    left: 185px;
    top: 903px;
    font-size: 52px;
    line-height: 1;
    color: var(--varietal-red);
  }
  .region {
    position: absolute;
    left: 739px;
    top: 900px;
    font-size: 54px;
    line-height: 1;
  }
  .alcohol {
    position: absolute;
    left: 682px;
    top: 985px;
    font-family: "Arimo", Arial, sans-serif;
    font-size: 36px;
    line-height: 1;
  }
</style>
</head>
<body>
  <main class="label">
    <div class="frame-outer"></div>
    <div class="frame-middle"></div>
    <div class="frame-inner"></div>

    <div class="vintage">2012</div>

    <div class="vineyard-scene" role="img" aria-label="Ink sketch of vineyard rows leading to striped rolling hills with trees, clouds and a small camper van on the hilltop"></div>

    <div class="brand-name">TALLHĂ´VE WINE CO.</div>

    <div class="varietal">CHENIN BLANC</div>
    <div class="region">Clarksburg</div>
    <div class="alcohol">Alc. 13.6% by vol.</div>
  </main>
</body>
</html>
```